Urine collection cup with and without sterile seal sticker

Hello. We need a urine cup label designed please with

Name:
Date of Birth:
Date:
Time:
Temp℃:
Specimen ID:

Product code: TUB-47
Volume markings (e.g., 30 mL, 60 mL, 90 mL).
Vela Drug Tests logo

Could you please provide one version with the additional sterile sticker extending to the top, and one version without the additional sterile sticker?

```html
<!DOCTYPE html>
<html lang="en">
<head>
<meta charset="utf-8">
<title>Vela Drug Tests – Urine Cup Labels</title>
<link href="https://fonts.googleapis.com/css2?family=Inter:wght@300;400&family=Roboto:wght@900&display=swap" rel="stylesheet">
<style>
  :root{
    --bg-light:#c2c2c2;
    --bg-dark:#8a8a8a;
    --label:#ffffff;
    --ink:#1f1f1f;
    --brand-blue:#2b9fe6;
    --strip-top:#5db7ea;
    --strip-bottom:#2a9fe6;
  }
  html,body{margin:0;padding:0;overflow:hidden}
  body{width:930px;height:1200px;background:radial-gradient(ellipse at 50% 55%,var(--bg-light),var(--bg-dark) 75%)}
  .sheet{display:block;width:930px;height:1200px}
  .label-body{fill:var(--label)}
  .field{font-family:"Inter",sans-serif;font-weight:400;font-size:24px;fill:var(--ink);letter-spacing:-0.8px}
  .rule{stroke:var(--ink);stroke-width:1.4}
  .vol-box{fill:none;stroke:var(--ink);stroke-width:1.4}
  .vol-text{font-family:"Inter",sans-serif;font-size:26px;fill:var(--ink);letter-spacing:-0.8px;text-anchor:middle}
  .brand-name{font-family:"Inter",sans-serif;font-weight:400;font-size:22px;fill:var(--ink);letter-spacing:-0.6px;text-anchor:end}
  .strip{fill:url(#stripGrad)}
  .strip-main{font-family:"Roboto",sans-serif;font-weight:900;font-size:28px;fill:#fff}
  .strip-sub{font-family:"Roboto",sans-serif;font-weight:900;font-size:26px;fill:#fff}
  .product-code{font-family:"Inter",sans-serif;font-weight:300;font-size:15px;fill:#fff}
  .sterile{font-family:"Roboto",sans-serif;font-weight:900;font-size:30px;fill:var(--brand-blue)}
  .esteril{font-family:"Roboto",sans-serif;font-weight:900;font-size:20px;fill:var(--brand-blue)}
</style>
</head>
<body>
<svg class="sheet" viewBox="0 0 930 1200" xmlns="http://www.w3.org/2000/svg">
  <defs>
    <linearGradient id="stripGrad" x1="0" y1="0" x2="0" y2="1">
      <stop offset="0" stop-color="var(--strip-top)"/>
      <stop offset="1" stop-color="var(--strip-bottom)"/>
    </linearGradient>
    <g id="form-fields">
      <text class="field" x="115" y="243">Name:</text>
      <text class="field" x="115" y="271">Nombre:</text>
      <line class="rule" x1="216" y1="271" x2="526" y2="271"/>
      <text class="field" x="115" y="317">Date of Birth:</text>
      <text class="field" x="115" y="346">Fecha de nacimiento:</text>
      <line class="rule" x1="358" y1="346" x2="668" y2="346"/>
      <text class="field" x="115" y="387">Date:</text>
      <text class="field" x="115" y="415">Fecha:</text>
      <line class="rule" x1="196" y1="415" x2="392" y2="415"/>
      <text class="field" x="410" y="387">Time:</text>
      <text class="field" x="410" y="415">Hora:</text>
      <line class="rule" x1="482" y1="415" x2="668" y2="415"/>
      <text class="field" x="115" y="458">Temp°C:</text>
      <text class="field" x="115" y="486">Temperatura°C:</text>
      <line class="rule" x1="285" y1="486" x2="594" y2="486"/>
      <text class="field" x="115" y="532">Specimen ID:</text>
      <text class="field" x="115" y="560">Identificación:</text>
      <line class="rule" x1="285" y1="560" x2="594" y2="560"/>
      <text class="field" x="115" y="607">Volume:</text>
      <text class="field" x="115" y="633">Volumen:</text>
      <rect class="vol-box" x="284" y="592" width="87" height="42" rx="5"/>
      <text class="vol-text" x="327.5" y="622">30mL</text>
      <rect class="vol-box" x="396" y="592" width="86" height="42" rx="5"/>
      <text class="vol-text" x="439" y="622">60mL</text>
      <rect class="vol-box" x="505" y="592" width="87" height="42" rx="5"/>
      <text class="vol-text" x="548.5" y="622">90mL</text>
      <text class="brand-name" x="729" y="240">Vela Drug Tests</text>
    </g>
    <g id="strip-text">
      <text class="strip-main" transform="translate(795,264) rotate(90)" textLength="324" lengthAdjust="spacingAndGlyphs">TIGHTEN CAP SECURELY</text>
      <text class="strip-sub" transform="translate(762,339) rotate(90)" textLength="174" lengthAdjust="spacingAndGlyphs">CERRAR BIEN</text>
    </g>
  </defs>

  <g class="label label--sterile">
    <path class="label-body" d="M107,198 H708 Q747,198 747,160 V92 A48,48 0 0 1 795,44 A47,47 0 0 1 842,91 V220 H747 V655 H107 Q89,655 89,637 V216 Q89,198 107,198 Z"/>
    <rect class="strip" x="747" y="220" width="95" height="435"/>
    <path class="strip" d="M724,655 V496 Q724,478 742,478 H748 V655 Z"/>
    <text class="sterile" transform="translate(795,69) rotate(90)" textLength="136" lengthAdjust="spacingAndGlyphs">STERILE</text>
    <text class="esteril" transform="translate(768,95) rotate(90)" textLength="85" lengthAdjust="spacingAndGlyphs">ESTERIL</text>
    <use href="#strip-text"/>
    <text class="product-code" transform="translate(731,491) rotate(90)">Product code: TUB-47</text>
    <use href="#form-fields"/>
  </g>

  <g class="label label--plain">
    <path class="label-body" d="M107,689 H747 V1147 H107 Q89,1147 89,1129 V707 Q89,689 107,689 Z"/>
    <path class="strip" d="M747,689 H824 Q842,689 842,707 V1129 Q842,1147 824,1147 H747 Z"/>
    <path class="strip" d="M724,1147 V988 Q724,970 742,970 H748 V1147 Z"/>
    <g transform="translate(0,491)">
      <use href="#strip-text"/>
      <text class="product-code" transform="translate(731,491) rotate(90)">Product code: TUB-47</text>
      <use href="#form-fields"/>
    </g>
  </g>
</svg>
</body>
</html>
```